NEED BILLBOARDS FOR VELMORANCIA

we need to redo our billboards for our business. we want to have catchy, great billboards that follow standard billboard design rules. we do breast and body cosmetic surgery in Bakersfield, fresno, and stockton ca. see attached for some tips. i would like something creative, but conservative, but funny. we also won finest around 18 years in a row and can give you the logo

Target Market(s)

females 21-45

Industry/Entity Type

plastic surgery of the breast and body

Font styles to use
Serif

Requirements
Nice to have
• funny, catchy
Should not have
• pictures of women that are overly exposed

```html
<!DOCTYPE html>
<html lang="en">
<head>
<meta charset="utf-8">
<title>Velmorancia Billboard</title>
<link rel="stylesheet" href="https://fonts.googleapis.com/css2?family=Crimson+Pro:wght@400;600;700&family=Open+Sans:wght@400&display=swap">
<style>
  :root {
    --stage: #eceef0;
    --rose: #e0525c;
    --rose-deep: #d94a55;
    --aqua: #a9d8df;
    --white: #ffffff;
    --photo-warm: #c98a68;
    --photo-hair: #8a4a2c;
    --brand-green: #6fb77a;
    --tag-pink: #d46a86;
    --url-blue: #6d86c6;
  }
  * { box-sizing: border-box; margin: 0; padding: 0; }
  html, body {
    width: 1200px;
    height: 808px;
    overflow: hidden;
    background: var(--stage);
  }
  .billboard {
    position: absolute;
    left: 20px;
    top: 181px;
    width: 1160px;
    height: 446px;
    overflow: hidden;
    background: linear-gradient(180deg,
      var(--rose) 0%,
      var(--rose-deep) 45%,
      var(--aqua) 68%,
      var(--white) 88%,
      var(--white) 100%);
  }
  .portrait {
    position: absolute;
    left: 22px;
    top: 0;
    width: 470px;
    height: 446px;
  }
  .headline {
    position: absolute;
    left: 510px;
    top: 28px;
    font-family: "Crimson Pro", Georgia, serif;
    font-weight: 700;
    font-size: 88px;
    line-height: 86px;
    color: var(--white);
    text-shadow: 2px 3px 5px rgba(0, 0, 0, 0.28);
    letter-spacing: 0.5px;
  }
  .brand {
    position: absolute;
    left: 512px;
    top: 340px;
  }
  .brand-name {
    font-family: "Crimson Pro", Georgia, serif;
    font-weight: 600;
    font-size: 40px;
    line-height: 40px;
    color: var(--brand-green);
    letter-spacing: 1px;
  }
  .brand-tagline {
    margin-top: 6px;
    font-family: "Open Sans", Arial, sans-serif;
    font-size: 9px;
    color: var(--tag-pink);
    letter-spacing: 0.2px;
  }
  .web-address {
    position: absolute;
    left: 845px;
    top: 336px;
    font-family: "Crimson Pro", Georgia, serif;
    font-weight: 700;
    font-size: 38px;
    color: var(--url-blue);
    letter-spacing: 0.5px;
  }
</style>
</head>
<body>
  <section class="billboard">
    <svg class="portrait" role="img" aria-label="Portrait photograph of a woman with long auburn hair" viewBox="0 0 470 446" preserveAspectRatio="none">
      <defs>
        <radialGradient id="portraitTone" cx="45%" cy="50%" r="60%">
          <stop offset="0%" stop-color="var(--photo-warm)"/>
          <stop offset="70%" stop-color="var(--photo-hair)"/>
          <stop offset="100%" stop-color="var(--photo-hair)" stop-opacity="0"/>
        </radialGradient>
      </defs>
      <rect width="470" height="446" fill="url(#portraitTone)"/>
    </svg>

    <h1 class="headline">Want to be the<br>hottest mom<br>on the block?</h1>

    <div class="brand">
      <div class="brand-name">Velmorancia</div>
      <div class="brand-tagline">COSMETIC SURGERY AND MEDICAL AESTHETICS</div>
    </div>

    <div class="web-address">velmorancia.com</div>
  </section>
</body>
</html>
```